Business Intelligence Application - Reporting Menu and Report Criteria Design

Looking for a fresh, effective and user friendly view for the menu structure and reporting criteria screen format for a business reporting application. Initial format completed, content structure is in place, but we need the 'wow' design.. as its a serious professional report/BI tool it has to fall within certain guidelines for clarity and graphics..but we want it to be slick, friendly, great user experience. There is a large amount of complex content to fit into a small space and we need it to be very inviting, modern and intuitive.. If interested, please review the attachment. We have live screens in operation, but feel these could be improved and looking forward to seeing what great creative suggestions could be made. Please review work done to date in the attached.. We are not looking for a total re-design of everything, all the basic business content/structure is there.. but tell us what we could do to improve this in terms of graphic design... particularly the criteria screens.. thanks!
Updates

Reason: Need a few more days to review designs - thanks for all submissions so far, we will make a selection shortly.

Target Market(s)

Business analysts, hotel operations teams, finance analysts hospitality industry

Industry/Entity Type

Hospitality

Coding

Coded - Design and coding required

Number of Pages Required

4 page

Font styles to use
Sans Serif
Other font styles liked:
• Candara, please see example in deck

Colors
3276b5
3176b5
0255a3
85acd3
33a6d7
cee9f5
85cae6

Requirements
Must have
• sharp clear, logical menu structure, (currently it has 'clicks to sub-menus, we need hover over, slide to sub-menus..) colour, styling.. and most focus on revision of criteria.. right now is somewhat heavy, cumbersome.. keep colour and friendly intuitive process steps.. its heavy analytical stuff.. best of luck!
Should not have
• No grey fonts on white or grey screens! many business apps are not readable or sharp.. or fonts are too small.. colourless, so please avoid that.. see our deck - sharp dark (navy) or black fonts on white, or light shading..

```html
<!DOCTYPE html>
<html lang="en">
<head>
<meta charset="utf-8">
<title>Halden Metrics – Property Search</title>
<link rel="stylesheet" href="https://fonts.googleapis.com/css2?family=Mulish:wght@400;600;700&family=Open+Sans:wght@400;600&display=swap">
<style>
  :root {
    --header-bg: #020f24;
    --nav-bg: #063a73;
    --nav-active: #1d5a83;
    --nav-text: #8fa1b5;
    --nav-divider: #2a5a8c;
    --body-top: #134a66;
    --body-bottom: #03234a;
    --panel-back: #17465e;
    --panel: #0255a3;
    --white: #ffffff;
    --brand: #8ea0b2;
    --welcome: #8a9099;
    --icon: #2f76b5;
    --divider: #0c2340;
    --footer-bg: #737373;
    --footer-text: #474747;
    --avatar: #6f6458;
    --mark: #2c8f94;
  }
  * { margin: 0; padding: 0; box-sizing: border-box; }
  html, body { width: 1200px; height: 664px; overflow: hidden; }
  body { position: relative; font-family: "Mulish", sans-serif; background: var(--body-bottom); }

  .app-header { position: absolute; left: 0; top: 0; width: 1200px; height: 113px; background: var(--header-bg); }
  .brand { position: absolute; left: 99px; top: 43px; display: flex; align-items: center; gap: 14px; }
  .brand-mark { width: 36px; height: 36px; border-radius: 50%; background: var(--mark); }
  .brand-name { font-family: "Open Sans", sans-serif; font-weight: 600; font-size: 27px; color: var(--brand); letter-spacing: 0.2px; }

  .user { position: absolute; left: 781px; top: 34px; display: flex; align-items: center; gap: 8px; }
  .avatar { width: 44px; height: 44px; border-radius: 50%; background: radial-gradient(circle at 50% 40%, #b9aa98, var(--avatar)); }
  .user-text { font-family: "Open Sans", sans-serif; font-size: 14px; line-height: 21px; color: var(--welcome); }
  .header-divider { position: absolute; top: 40px; width: 1px; height: 38px; background: var(--divider); }
  .header-icon { position: absolute; top: 42px; }

  .main-nav { position: absolute; left: 0; top: 113px; width: 1200px; height: 51px; background: var(--nav-bg); }
  .main-nav ul { list-style: none; position: absolute; left: 83px; top: 0; height: 51px; display: flex; }
  .main-nav li { height: 51px; display: flex; align-items: center; padding: 0 7px; font-size: 13px; font-weight: 700; color: var(--nav-text); border-left: 1px solid var(--nav-divider); white-space: nowrap; }
  .main-nav li:first-child { border-left: none; }
  .main-nav li.is-active { background: var(--nav-active); gap: 4px; }
  .nav-badge { width: 20px; height: 20px; border-radius: 50%; background: #b07a3c; }

  .content { position: absolute; left: 0; top: 164px; width: 1200px; height: 424px; background: linear-gradient(180deg, var(--body-top) 0%, var(--body-bottom) 100%); }
  .panel-back { position: absolute; left: 112px; top: 19px; width: 974px; height: 320px; background: var(--panel-back); }
  .results { position: absolute; left: 142px; top: 8px; width: 945px; height: 306px; background: var(--panel); color: var(--white); }
  .results h1 { position: absolute; left: 52px; top: 38px; font-size: 17px; font-weight: 700; letter-spacing: 0.2px; }
  .result-col { position: absolute; top: 90px; list-style: none; }
  .result-col li { position: relative; padding-left: 13px; height: 32.6px; font-size: 14px; line-height: 20px; }
  .result-col li::before { content: ""; position: absolute; left: 0; top: 5px; border-left: 5px solid var(--white); border-top: 5px solid transparent; border-bottom: 5px solid transparent; }

  .app-footer { position: absolute; left: 0; top: 588px; width: 1200px; height: 76px; background: var(--footer-bg); font-family: "Open Sans", sans-serif; font-size: 13px; color: var(--footer-text); text-align: center; padding-top: 24px; padding-left: 50px; word-spacing: 1px; }
</style>
</head>
<body>
  <header class="app-header">
    <div class="brand">
      <span class="brand-mark"></span>
      <span class="brand-name">Halden Metrics</span>
    </div>
    <div class="user">
      <div class="avatar" role="img" aria-label="User profile photo"></div>
      <div class="user-text">Welcome<br>Admin</div>
    </div>
    <span class="header-divider" style="left:919px"></span>
    <svg class="header-icon" style="left:946px" width="28" height="28" viewBox="0 0 24 24" aria-label="Notifications">
      <path fill="var(--icon)" d="M12 2a1.6 1.6 0 0 1 1.6 1.6v.6A6.5 6.5 0 0 1 18.5 10.5v4.5l2.3 3H3.2l2.3-3v-4.5A6.5 6.5 0 0 1 10.4 4.2v-.6A1.6 1.6 0 0 1 12 2zm-2.6 17h5.2a2.6 2.6 0 0 1-5.2 0z"/>
    </svg>
    <span class="header-divider" style="left:1004px"></span>
    <svg class="header-icon" style="left:1034px" width="30" height="26" viewBox="0 0 24 20" aria-label="Log out">
      <path fill="var(--icon)" d="M14 1l9 7.5-9 7.5v-4.5C7.5 11.5 3.5 13.5 1 18c.8-6.5 4.5-11.5 13-12.5z"/>
    </svg>
  </header>

  <nav class="main-nav">
    <ul>
      <li>Admin</li>
      <li>Management</li>
      <li>Rooms Performance</li>
      <li>Revenue Summary</li>
      <li>Demand &amp; Risk</li>
      <li>Inventory Analysis</li>
      <li>Placeholder</li>
      <li class="is-active"><span class="nav-badge" role="img" aria-label="Property search mascot icon"></span>Property Search</li>
      <li>Intel</li>
      <li>Planning</li>
    </ul>
  </nav>

  <main class="content">
    <div class="panel-back"></div>
    <section class="results">
      <h1>SEARCH RESULT</h1>
      <ul class="result-col" style="left:52px">
        <li>Harrowgate Hotel</li>
        <li>Grand Harrowgate Hotel</li>
        <li>Riverside Quay Hotel</li>
        <li>Central Wharf Hotel</li>
        <li>Sociosqu ad litora</li>
      </ul>
      <ul class="result-col" style="left:280px">
        <li>Torquent per</li>
        <li>Conubia nostra</li>
        <li>Per inceptos hymenaeos</li>
        <li>Donec quis mi sed</li>
        <li>Aagna hendrerit</li>
      </ul>
      <ul class="result-col" style="left:519px">
        <li>Suspendisse risus nibh</li>
        <li>Nltricies eu volutpat</li>
        <li>Non condimentum</li>
        <li>Pendrerit augue</li>
        <li>Etiam eleifend</li>
      </ul>
      <ul class="result-col" style="left:746px">
        <li>Metus vitae</li>
        <li>Adipiscing semper</li>
        <li>Pauris ipsum iaculis</li>
        <li>Elit congue</li>
        <li>Gravida elit mi</li>
      </ul>
    </section>
  </main>

  <footer class="app-footer">© 2017 Company Name &nbsp;All right reserved &nbsp;Term of Use</footer>
</body>
</html>
```